Web Design Project - brivocell

I'm building an agency for marketing solutions but also medical education and patients education for pharmaceutical companies, medical societies and patient advocacy groups. We want to be perceived as the most innovative in the market. We work through design thinking solutions for campaigns and services.
I love some websites based on Swiss style design like www.plumvane.example
We are a small group of designers, physicians and creatives working together to deliver the best experiences in our market.
We decided to also use pixel forum expecting that we maybe found a great idea we didn't thought about yet.

I'm extending it for more 2 weeks

Reason: I need the best design you can. Only PSD. No code needed. Love Swiss style, like tessera 5 and plumvane.example I'm extending the deadline until get something great. Willing to extend as much as needed.

Target Market(s)

Pharmaceutical companies, physicians, medical societies, patients advocacy groups

Industry/Entity Type

Pharmaceutical

Font styles to use
Other font styles liked:
• Helvetia family

Colors

Designer to choose colors to be used in the design.

Requirements
Must have
• Must be innovative like www.plumvane.example
Nice to have
• Cool menus
Should not have
• Not to appear too much Comercial. We like to be a boutique in this market. Craftsmen working with less clients at time but delivering precious stones.

```html
<!DOCTYPE html>
<html lang="en">
<head>
<meta charset="utf-8">
<title>brivocell</title>
<link rel="stylesheet" href="https://fonts.googleapis.com/css2?family=Open+Sans:ital,wght@0,300;0,400;0,600;0,700;1,600&family=Roboto+Condensed:wght@400;700&display=swap">
<style>
:root{
  --ink:#0b1120;
  --panel:#0d1a33;
  --frame:#1b74dc;
  --accent:#1e8ae8;
  --link:#2c8cf0;
  --white:#ffffff;
  --muted:#aab4c4;
  --tab-dark:#111723;
  --footer:#0c0f16;
  --band:#1466c8;
  --hot:#e2583c;
}
*{box-sizing:border-box;margin:0;padding:0}
html,body{width:1200px;height:3822px;overflow:hidden}
body{position:relative;background:var(--ink);font-family:"Open Sans",Arial,sans-serif;color:var(--white)}
.layer{position:absolute;left:0;width:1200px}
.hero-bg{top:0;height:690px;background:radial-gradient(ellipse at 70% 30%,#3a2a55 0%,#14182e 45%,#070a14 100%)}
.sky-bg{top:690px;height:1380px;background:linear-gradient(180deg,#7d8aa0 0%,#4e5b72 30%,#2b3447 60%,#1b2130 100%)}
.city-bg{top:2070px;height:1255px;background:linear-gradient(180deg,#2a3140 0%,#151a24 50%,#0a0d14 100%)}

.site-nav{position:absolute;top:0;left:0;width:1200px;height:90px;display:flex;align-items:center;padding:0 100px 0 115px}
.brand{font-family:"Roboto Condensed",Arial,sans-serif;font-weight:700;font-size:26px;color:var(--white)}
.nav-links{margin-left:auto;display:flex;gap:48px;align-items:center;font-size:16px}
.nav-links a{color:var(--white);text-decoration:none}
.nav-links .login{border:2px solid var(--white);border-radius:6px;padding:6px 34px;margin-left:20px}

.hero{position:absolute;top:200px;left:0;width:1200px;text-align:center}
.hero h1{font-weight:300;font-size:46px;letter-spacing:1px}
.hero .lead{font-size:17px;line-height:26px;margin-top:12px;color:#e4e8f2}
.play{display:block;margin:30px auto 0}
.hero .cta-line{margin-top:30px;font-size:18px}
.hero .note{font-size:11px;color:var(--muted);margin-top:2px}
.button{display:inline-block;background:var(--accent);color:var(--white);font-size:15px;font-weight:600;letter-spacing:1px;padding:8px 26px;text-decoration:none;white-space:nowrap}
.hero .button{margin-top:34px}

.tabbar{position:absolute;left:107px;width:993px;height:85px;display:flex}
.tab-main{width:333px;background:var(--white);color:var(--ink);display:flex;align-items:center;gap:14px;padding-left:26px;font-family:"Roboto Condensed",Arial,sans-serif;font-size:34px}
.tab-side{flex:1;background:var(--tab-dark);display:flex;align-items:center;padding:0 24px 0 34px;font-family:"Roboto Condensed",Arial,sans-serif;font-size:34px}
.tab-side .tail{margin-left:auto;display:flex}
.social-sq{width:52px;height:85px;display:flex;align-items:center;justify-content:center;background:var(--tab-dark)}
.social-sq.light{background:var(--white)}

.grid-frame{position:absolute;left:107px;width:993px;height:835px;background:var(--frame);padding:14px;display:grid;grid-template-columns:repeat(3,1fr);grid-template-rows:repeat(3,1fr);gap:8px}
.cell{background:var(--panel);padding:20px 22px;overflow:hidden}
.cell.light{background:var(--white);color:var(--ink)}
.cell.tall{grid-row:span 2}
.cell h3{font-family:"Roboto Condensed",Arial,sans-serif;font-weight:700;font-size:40px;line-height:44px}
.cell p{font-size:12.5px;font-weight:700;line-height:17px;margin-top:10px}
.cell .aside{font-style:italic;font-weight:600;color:var(--link)}
.more{flex:none;display:inline-flex;align-items:center;gap:8px;background:var(--white);color:var(--ink);font-size:12px;font-weight:700;padding:4px 8px;border:2px solid var(--ink);white-space:nowrap}
.cell .foot{display:flex;align-items:flex-end;justify-content:space-between;gap:12px}
.p-crowd{background:linear-gradient(160deg,#c9c4bb,#6f6a63 60%,#3a3733)}
.p-store{background:linear-gradient(160deg,#e8edf2,#6fa6d0 50%,#2d5c8a)}
.p-hand{background:linear-gradient(160deg,#b9b4ad,#5f5a54 60%,#2a2724)}
.p-man{background:linear-gradient(160deg,#d7ccbd,#8a7258 60%,#3d3024)}
.p-woman{background:linear-gradient(160deg,#d9e3d2,#b59a86 55%,#6c5244)}
.p-woman2{background:linear-gradient(160deg,#6a5a52,#b0504a 55%,#5a1f1c)}
.person{display:flex;flex-direction:column;justify-content:center;align-items:center;text-align:center}
.person h4{font-family:"Roboto Condensed",Arial,sans-serif;font-weight:700;font-size:44px;line-height:46px}
.person .role{font-size:12px;font-weight:700;color:#c4cddc}
.person .links{display:flex;margin-top:14px}

.feature{position:absolute;left:0;width:1200px;text-align:center}
.feature .kicker{font-size:15px;letter-spacing:6px;color:#e8ecf4}
.feature h2{font-weight:300;font-size:48px;letter-spacing:3px;line-height:54px}
.feature p.body{width:800px;margin:10px auto 0;font-size:12.5px;line-height:17px;color:#d7dde8}
.feature .button{margin-top:26px}

.info-band{position:absolute;top:3325px;left:0;width:1200px;height:250px;background:var(--band);display:flex;gap:60px;padding:24px 0 0 218px}
.info-col{width:200px;font-size:11px;line-height:15px;color:#dbe8fa}
.info-col h5{font-size:12px;font-weight:700;color:var(--white);letter-spacing:1px;margin-bottom:8px}
.blog{width:240px}
.blog-item{display:flex;gap:10px;margin-bottom:12px}
.thumb{width:44px;height:32px;flex:none;background:linear-gradient(135deg,#9fb6d3,#46607f)}

.site-footer{position:absolute;top:3575px;left:0;width:1200px;height:247px;background:var(--footer);display:flex;padding:36px 0 0 248px}
.footer-brand{width:222px}
.footer-brand p{font-size:10.5px;line-height:15px;color:var(--muted);margin-top:12px;width:180px}
.footer-col{width:146px;font-size:11px;line-height:17px;color:var(--muted)}
.footer-col h6{font-size:12px;font-weight:700;color:var(--hot);margin-bottom:6px}
</style>
</head>
<body>

<div class="layer hero-bg" role="img" aria-label="Dark night backdrop with a glowing network of connected points"></div>
<div class="layer sky-bg" role="img" aria-label="Aircraft on a runway under a cloudy sky"></div>
<div class="layer city-bg" role="img" aria-label="Aerial view of a city skyline at dusk"></div>

<header class="site-nav">
  <div class="brand">brivocell</div>
  <nav class="nav-links">
    <a href="#">Home</a><a href="#">News</a><a href="#">Events</a><a href="#" class="login">Login</a>
  </nav>
</header>

<section class="hero">
  <h1>CRAFTED CLINICAL CLARITY</h1>
  <p class="lead">brivocell designs everything your medical team needs to<br>ensure every patient and physician truly understands.</p>
  <svg class="play" width="62" height="62" viewBox="0 0 62 62"><circle cx="31" cy="31" r="28" fill="none" stroke="#fff" stroke-width="3"/><path d="M25 19 L44 31 L25 43 Z" fill="#fff"/></svg>
  <p class="cta-line">Start your next campaign with us today!</p>
  <p class="note">Few clients at a time, by design</p>
  <a class="button" href="#">VISIT OUR STUDIO!</a>
</section>

<div class="tabbar" style="top:680px">
  <div class="tab-main">
    <svg width="34" height="30" viewBox="0 0 34 30"><rect x="2" y="3" width="30" height="24" fill="none" stroke="#0b1120" stroke-width="3"/><path d="M7 10h10M7 15h20M7 20h20" stroke="#0b1120" stroke-width="3"/></svg>
    RECENT NEWS
  </div>
  <div class="tab-side">STAY CONNECTED</div>
  <div class="social-sq light"><svg width="20" height="20"><circle cx="10" cy="10" r="8" fill="none" stroke="#111723" stroke-width="2"/></svg></div>
  <div class="social-sq"><svg width="20" height="20"><circle cx="10" cy="10" r="8" fill="none" stroke="#fff" stroke-width="2"/></svg></div>
</div>

<section class="grid-frame" style="top:765px">
  <div class="p-crowd" role="img" aria-label="People walking along a busy city pavement"></div>
  <article class="cell">
    <h3>Header News!</h3>
    <p>Lorem Ipsum is simply dummy text of the printing and typesetting industry. Lorem Ipsum has been the industry's standard dummy text ever since the 1500s.</p>
    <p class="aside">When an unknown printer took a galley of type and scrambled it to make a type specimen book.</p>
  </article>
  <article class="cell">
    <h3>Header News!</h3>
    <p>Lorem Ipsum is simply dummy text of the printing and typesetting industry. Lorem Ipsum has been the industry's standard dummy text ever since the 1500s.</p>
    <div class="foot"><p class="aside">When an unknown printer took a galley of type and scrambled it to make a specimen.</p><span class="more">See More <svg width="12" height="12"><circle cx="6" cy="6" r="6" fill="#1b74dc"/><path d="M4 3l4 3-4 3" stroke="#fff" fill="none" stroke-width="1.5"/></svg></span></div>
  </article>
  <article class="cell light tall">
    <h3>Header News!</h3>
    <p>Lorem Ipsum is simply dummy text of the printing and typesetting industry. Lorem Ipsum has been the industry's standard dummy text ever since the 1500s.</p>
    <p class="aside">When an unknown printer took a galley of type and scrambled it to make a type specimen book.</p>
    <p>It has survived not only five centuries, but also the leap into electronic typesetting, remaining essentially unchanged. It was popularised.</p>
    <div class="foot"><p class="aside">Lorem Ipsum is simply dummy text of the printing and typesetting industry. Lorem Ipsum has been the industry.</p><span class="more">See More <svg width="12" height="12"><circle cx="6" cy="6" r="6" fill="#1b74dc"/><path d="M4 3l4 3-4 3" stroke="#fff" fill="none" stroke-width="1.5"/></svg></span></div>
  </article>
  <div class="p-store" role="img" aria-label="Shop front with a blue striped awning"></div>
  <article class="cell">
    <h3>Header News!</h3>
    <p>Lorem Ipsum is simply dummy text of the printing and typesetting industry. Lorem Ipsum has been the industry's standard dummy text ever since the 1500s.</p>
    <p class="aside">When an unknown printer took a galley of type and scrambled it to make a type specimen book.</p>
  </article>
  <article class="cell">
    <h3>Header News!</h3>
    <p>Lorem Ipsum is simply dummy text of the printing and typesetting industry. Lorem Ipsum has been the industry's standard dummy text ever since the 1500s.</p>
    <p class="aside">When an unknown printer took a galley of type and scrambled it to make a type specimen book.</p>
  </article>
  <div class="p-hand" role="img" aria-label="Hand holding a strap on a train"></div>
</section>

<section class="feature" style="top:1712px">
  <p class="kicker">FOR A CLEARER CONVERSATION</p>
  <h2>DESIGN THINKING</h2>
  <p class="body">We sit with physicians, patients and advocacy groups before we sketch a single screen. Every campaign begins with listening, mapping real journeys and testing ideas early, so that medical education feels human, precise and calm. Small teams, few clients and careful craft let us polish each detail until it truly serves the people who rely on it.</p>
  <a class="button" href="#">VISIT OUR STUDIO!</a>
</section>

<div class="tabbar" style="top:2075px">
  <div class="tab-main">
    <svg width="32" height="32" viewBox="0 0 32 32"><circle cx="16" cy="11" r="7" fill="none" stroke="#0b1120" stroke-width="3"/><path d="M3 30c2-8 8-11 13-11s11 3 13 11" fill="none" stroke="#0b1120" stroke-width="3"/></svg>
    MEET THE CREW
  </div>
  <div class="tab-side">DON'T HESITATE TO CONTACT
    <span class="tail"><svg width="34" height="30" viewBox="0 0 34 30"><path d="M2 14 L32 2 L24 28 L16 18 Z M16 18 L32 2" fill="none" stroke="#fff" stroke-width="2.5" stroke-linejoin="round"/></svg></span>
  </div>
</div>

<section class="grid-frame" style="top:2160px">
  <div class="p-man" role="img" aria-label="Portrait of a smiling team member"></div>
  <article class="cell person">
    <h4>John Smith</h4>
    <p class="role">Co-founder and Medical Director</p>
    <div class="links"><svg width="64" height="14"><circle cx="7" cy="7" r="6" fill="#fff"/><circle cx="32" cy="7" r="6" fill="#fff"/><circle cx="57" cy="7" r="6" fill="#fff"/></svg></div>
  </article>
  <article class="cell">
    <h3>Header News!</h3>
    <p>Lorem Ipsum is simply dummy text of the printing and typesetting industry. Lorem Ipsum has been the industry's standard dummy text ever since the 1500s.</p>
    <div class="foot"><p class="aside">When an unknown printer took a galley of type and scrambled it to make a specimen.</p><span class="more">See More <svg width="12" height="12"><circle cx="6" cy="6" r="6" fill="#1b74dc"/><path d="M4 3l4 3-4 3" stroke="#fff" fill="none" stroke-width="1.5"/></svg></span></div>
  </article>
  <article class="cell light tall">
    <h3>Header News!</h3>
    <p>Lorem Ipsum is simply dummy text of the printing and typesetting industry. Lorem Ipsum has been the industry's standard dummy text ever since the 1500s.</p>
    <p class="aside">When an unknown printer took a galley of type and scrambled it to make a type specimen book.</p>
    <p>It has survived not only five centuries, but also the leap into electronic typesetting, remaining essentially unchanged. It was popularised.</p>
    <div class="foot"><p class="aside">Lorem Ipsum is simply dummy text of the printing and typesetting industry. Lorem Ipsum has been the industry.</p><span class="more">See More <svg width="12" height="12"><circle cx="6" cy="6" r="6" fill="#1b74dc"/><path d="M4 3l4 3-4 3" stroke="#fff" fill="none" stroke-width="1.5"/></svg></span></div>
  </article>
  <div class="p-woman" role="img" aria-label="Portrait of a smiling team member outdoors"></div>
  <article class="cell person">
    <h4>Jane Smith</h4>
    <p class="role">Co-founder and Design Lead</p>
    <div class="links"><svg width="64" height="14"><circle cx="7" cy="7" r="6" fill="#fff"/><circle cx="32" cy="7" r="6" fill="#fff"/><circle cx="57" cy="7" r="6" fill="#fff"/></svg></div>
  </article>
  <article class="cell person">
    <h4>Jane Smith</h4>
    <p class="role">Patient Education Strategist</p>
    <div class="links"><svg width="64" height="14"><circle cx="7" cy="7" r="6" fill="#fff"/><circle cx="32" cy="7" r="6" fill="#fff"/><circle cx="57" cy="7" r="6" fill="#fff"/></svg></div>
  </article>
  <div class="p-woman2" role="img" aria-label="Portrait of a team member in a red top"></div>
</section>

<section class="feature" style="top:3068px">
  <p class="kicker">FOR EVERY PATIENT JOURNEY</p>
  <h2>MEDICAL EDUCATION</h2>
  <p class="body">From congress programmes for medical societies to plain-language guides for patients, we turn complex science into material people can use. Physicians on our team review every claim, designers shape every page, and each piece is tested with the audience it serves before it goes out into the world.</p>
  <a class="button" href="#" style="margin-top:18px">VISIT OUR STUDIO!</a>
</section>

<section class="info-band">
  <div class="info-col">
    <h5>OUR APPROACH</h5>
    <p>We take on only a few partners at a time, so every project gets senior attention from brief to launch.</p>
  </div>
  <div class="info-col">
    <h5>TESTIMONIALS</h5>
    <p>"Our society felt heard from the very first workshop. The materials were thoughtful, precise and on time."</p>
  </div>
  <div class="info-col blog">
    <h5>BLOG NEWS</h5>
    <div class="blog-item"><span class="thumb" role="img" aria-label="Blog post thumbnail"></span><p>Notes from the studio: designing calm patient journeys.</p></div>
    <div class="blog-item"><span class="thumb" role="img" aria-label="Blog post thumbnail"></span><p>Why small teams craft better medical education.</p></div>
  </div>
</section>

<footer class="site-footer">
  <div class="footer-brand">
    <div class="brand">brivocell</div>
    <p>A boutique studio of designers, physicians and creatives shaping clear, careful experiences for health.</p>
  </div>
  <div class="footer-col"><h6>About Us</h6><p>Studio<br>Team<br>Method<br>Journal<br>Careers</p></div>
  <div class="footer-col"><h6>Services</h6><p>Campaigns<br>Medical Education<br>Patient Guides<br>Congress Design<br>Digital Tools</p></div>
  <div class="footer-col"><h6>Partners</h6><p>Pharma<br>Societies<br>Physicians<br>Advocacy<br>Research</p></div>
  <div class="footer-col"><h6>Follow Us</h6><p>Journal<br>Newsletter<br>Podcast<br>Events<br>Archive</p></div>
</footer>

</body>
</html>
```